A5 flyer recto (just the front side) announcing the summer events

For a public aquarium in France, we invite you to create our A5 flyer recto (just the front side) announcing the events of this summer 2015
The flyer must be written in french, you will find attached all the text that you have to fill in the flyer.
You also have to use our logo in the top or in the bottom of the flyer (2 versions of the logo four color or black and white version. According your design you can use one of them)
We also have a mascot ( a sea horse), you can use it if you want to illustrate your design (attachment file)
We manage a mini-golf and we want to promote it with a special discount, you have to mentioned this benefit in the flyer as a special discount coupon)
You must specify our website and our adress..
We remain at your disposal for any question

```html
<!DOCTYPE html>
<html lang="fr">
<head>
<meta charset="utf-8">
<title>Aquarium des Vagues – Votre été 2015</title>
<link rel="stylesheet" href="https://fonts.googleapis.com/css2?family=Roboto+Condensed:wght@400;700&family=Open+Sans:ital,wght@0,400;0,700;1,400&display=swap">
<style>
  :root {
    --ocean-deep: #0a3f86;
    --ocean-mid: #1f6fbf;
    --sky-top: #8fd2f3;
    --sky-bottom: #dcf2fb;
    --title-yellow: #fbf47c;
    --ink: #111111;
    --text-soft: #333333;
    --green: #2f8a2a;
    --coupon-bg: #b6d98c;
    --dash: #6a6a6a;
    --white: #ffffff;
  }
  * { box-sizing: border-box; margin: 0; padding: 0; }
  html, body { width: 771px; height: 1200px; overflow: hidden; }
  body { background: var(--white); }
  .flyer {
    position: relative;
    width: 771px;
    height: 1200px;
    overflow: hidden;
    background: linear-gradient(180deg, var(--sky-top) 0%, var(--sky-bottom) 100%);
    font-family: "Roboto Condensed", "Arial Narrow", sans-serif;
  }
  .hero {
    position: absolute; left: 0; top: 0; width: 771px; height: 212px;
    background:
      radial-gradient(ellipse 260px 170px at 660px 150px, rgba(184,154,98,.85), rgba(184,154,98,0) 70%),
      linear-gradient(180deg, var(--ocean-mid) 0%, var(--ocean-deep) 70%, #0d3a52 100%);
  }
  .site-top {
    position: absolute; right: 32px; top: 16px;
    font-family: "Open Sans", Arial, sans-serif; font-weight: 700;
    font-size: 32px; color: var(--white); letter-spacing: -0.3px;
  }
  .title {
    position: absolute; left: 40px; top: 84px;
    font-weight: 700; font-size: 73px; line-height: 1;
    color: var(--title-yellow); letter-spacing: 0.5px;
  }
  .mascot {
    position: absolute; left: 462px; top: 262px; width: 258px; height: 632px;
    border-radius: 130px 130px 60px 60px;
    background: linear-gradient(180deg, rgba(185,225,167,.85), rgba(185,225,167,.35));
  }
  .events {
    position: absolute; left: 93px; top: 274px; width: 610px;
    list-style: none;
  }
  .events li {
    position: relative; padding-left: 13px;
    font-weight: 700; font-size: 23.4px; line-height: 28.5px; color: var(--ink);
    margin-bottom: 15px;
  }
  .events li::before {
    content: ""; position: absolute; left: 0; top: 11px;
    width: 7px; height: 7px; border-radius: 50%; background: var(--green);
  }
  .address {
    position: absolute; left: 89px; top: 805px;
    font-family: "Open Sans", Arial, sans-serif; font-size: 18.5px; line-height: 30px;
    color: var(--text-soft); font-style: normal;
  }
  .info {
    position: absolute; left: 89px; top: 893px; width: 600px;
    font-family: "Open Sans", Arial, sans-serif; font-weight: 700;
    font-size: 17.5px; line-height: 25px; color: var(--green);
  }
  .site-bottom {
    position: absolute; left: 89px; top: 947px;
    font-family: "Open Sans", Arial, sans-serif; font-weight: 700;
    font-size: 27px; color: var(--green);
  }
  .brand {
    position: absolute; left: 469px; top: 930px; width: 213px; height: 126px;
    background: var(--white);
    display: flex; align-items: center; justify-content: center; gap: 8px;
    font-weight: 700; font-size: 24px; line-height: 1.1; color: var(--ocean-mid); text-align: center;
  }
  .brand .dot { width: 16px; height: 16px; border-radius: 50%; background: var(--green); flex: none; }
  .cut-line {
    position: absolute; left: 0; top: 1072px; width: 771px; height: 0;
    border-top: 3px dashed var(--dash);
  }
  .scissors { position: absolute; left: 30px; top: 1040px; }
  .coupon {
    position: absolute; left: 49px; top: 1080px; width: 703px; height: 120px;
    background: var(--coupon-bg);
    padding: 22px 20px 0 8px;
    font-family: "Open Sans", Arial, sans-serif; color: var(--text-soft);
  }
  .coupon p { font-size: 15.5px; line-height: 23px; margin-left: 8px; }
  .coupon .note { font-style: italic; font-size: 12.5px; margin-top: 12px; }
</style>
</head>
<body>
<main class="flyer">
  <div class="hero" role="img" aria-label="Photographie sous-marine : eau bleue profonde et corail"></div>
  <div class="site-top">aquariumdesvagues.fr</div>
  <h1 class="title">Votre été 2015</h1>

  <div class="mascot" role="img" aria-label="Mascotte hippocampe vert clair"></div>

  <ul class="events">
    <li>Tous les jours, animations « bassin tactile » commentées</li>
    <li>Tous les après-midis Nourrissages commentés de nos espèces aquatiques</li>
    <li>Les mardis 21 &amp; 28 juillet, 4 &amp; 11 août de 20h à 23h, les Nocturnes de l’aquarium, avis de tempête</li>
    <li>Découvrez l’aquarium des Vagues comme vous ne l’avez jamais visité. 4 comédiens investissent l’aquarium pour une visite drôle et décalée à faire en famille</li>
    <li>Les jeudis 9 &amp; 16 juillet, 20 &amp; 27 août de 14h à 17h, pour les enfants de 6 à 12 ans,<br>l’aquarium propose des ateliers scientifiques. En compagnie d’un animateur, l’occasion d’apprendre en s’amusant</li>
    <li>En juillet &amp; août, Exposition « Laisse de Mer, source de vie » de Claire Morvan, Mieux comprendre la laisse de mer, son rôle écologique, son utilité pour nos plages…</li>
  </ul>

  <address class="address">
    Aquarium des Vagues<br>
    14, rue des Mouettes, 99120 LORVAN, 02 00 12 34 56
  </address>

  <p class="info">Retrouvez toutes les informations, tarif, horaires et conditions d’inscriptions sur :</p>
  <p class="site-bottom">aquariumdesvagues.fr</p>

  <div class="brand"><span class="dot"></span><span>Aquarium<br>des Vagues</span></div>

  <div class="cut-line"></div>
  <svg class="scissors" width="66" height="46" viewBox="0 0 66 46" aria-hidden="true">
    <circle cx="12" cy="10" r="8" fill="none" stroke="#111" stroke-width="3"/>
    <circle cx="12" cy="36" r="8" fill="none" stroke="#111" stroke-width="3"/>
    <path d="M18 15 L62 34 M18 31 L62 12" stroke="#111" stroke-width="3.5" stroke-linecap="round"/>
  </svg>

  <section class="coupon">
    <p>Sur présentation de ce coupon, bénéficiez d’une partie mini-golf enfant offerte pour une partie mini-golf adulte achetée *</p>
    <p class="note">*offre non cumulable avec toute autre promotion</p>
  </section>
</main>
</body>
</html>
```